Natural and organic skincare brand needs label design!

I need labels designed for my natural and organic skincare brand lumavale. The front of the bottles must contain the logo (image attached) and the following words: Formulated by a Naturopath; Anti-aging therapy; Organic Facial Oil; with CoEnzyme Q10 and Rosehip Seed Oil; 100ml e3.38fl.oz. Colours I would like used include black/white/grey/silver and aqua. I also like the grey woodgrain used on my draft website (check out www.lumavale-skin.com.au). The logo should be silver foil (shiny).The final design should be simple and communicate nature and sophistication. Some designs I like are found in the attachments. I intend to use black or white bottles.

Target Market(s)

women aged 30-50 interested in natural products

Industry/Entity Type

Skin Care Product

Font styles to use
Serif
Sans Serif
Decorative
Script
Other font styles liked:
• Any

Requirements
Must have
• Dimensions: 62mm (w) x 75mm (H) (front label only)
• Must contain the logo (image attached). The logo should be silver foil (shiny). and the following words are to be included on the label:
• Formulated by a Naturopath;
• Anti-aging Therapy;
• Organic Facial Oil;
• with CoEnzyme Q10 and Rosehip Seed Oil;
• 100ml e3.38fl.oz.
Nice to have
• Colours I would like used include black/white/grey/silver and aqua (turquoise). But I am also open to suggestion. I also like the grey woodgrain used on my draft website (check out www.lumavale-skin.com.au)

```html
<!DOCTYPE html>
<html lang="en">
<head>
<meta charset="utf-8">
<title>lumavale — Organic Facial Oil label</title>
<link rel="stylesheet" href="https://fonts.googleapis.com/css2?family=Cinzel:wght@400&family=Cormorant+Garamond:wght@400;500&family=Courier+Prime&display=swap">
<style>
  :root {
    --page: #e6e6e8;
    --label: #fbfbfa;
    --aqua: #bcd8cd;
    --aqua-line: #8fc2b2;
    --ink: #6f7072;
    --ink-soft: #8a8b8d;
    --white: #ffffff;
  }
  html, body {
    margin: 0;
    width: 1187px;
    height: 1200px;
    overflow: hidden;
    background: var(--page);
  }
  .label {
    position: absolute;
    left: 243px;
    top: 176px;
    width: 700px;
    height: 847px;
    background: var(--label);
    box-shadow: 0 2px 10px rgba(0,0,0,0.08);
    overflow: hidden;
    font-variant-numeric: lining-nums;
  }
  .tagline {
    position: absolute;
    top: 86px;
    width: 100%;
    margin: 0;
    text-align: center;
    font-family: "Courier Prime", monospace;
    font-size: 20px;
    letter-spacing: 2px;
    color: var(--ink);
  }
  .brand {
    position: absolute;
    top: 126px;
    width: 100%;
    display: flex;
    align-items: center;
    justify-content: center;
    gap: 14px;
  }
  .brand-dot {
    width: 16px;
    height: 16px;
    border-radius: 50%;
    background: var(--ink-soft);
  }
  .brand-name {
    font-family: "Cormorant Garamond", serif;
    font-weight: 500;
    font-size: 48px;
    line-height: 1;
    color: var(--ink);
  }
  .accent-strip {
    position: absolute;
    top: 232px;
    left: 0;
    width: 100%;
    height: 22px;
    background: var(--aqua);
  }
  .subtitle {
    position: absolute;
    top: 318px;
    width: 100%;
    margin: 0;
    text-align: center;
    font-family: "Cormorant Garamond", serif;
    font-size: 36px;
    color: var(--ink);
  }
  .subtitle::before, .subtitle::after {
    content: "";
    display: inline-block;
    width: 44px;
    height: 2px;
    background: var(--ink-soft);
    vertical-align: middle;
    margin: 0 14px;
  }
  .product-name {
    position: absolute;
    top: 370px;
    width: 100%;
    margin: 0;
    text-align: center;
    font-family: "Cinzel", serif;
    font-weight: 400;
    color: var(--ink);
    line-height: 1;
  }
  .product-name .primary {
    display: block;
    font-size: 96px;
    letter-spacing: 1px;
  }
  .product-name .secondary {
    display: block;
    font-size: 44px;
    margin-top: 4px;
  }
  .ingredients {
    position: absolute;
    top: 528px;
    left: 50%;
    transform: translateX(-50%);
    margin: 0;
    white-space: nowrap;
    border: 2px solid var(--aqua-line);
    padding: 6px 12px;
    font-family: "Cormorant Garamond", serif;
    font-weight: 500;
    font-size: 22px;
    color: var(--ink);
  }
  .volume-band {
    position: absolute;
    top: 640px;
    left: 0;
    width: 100%;
    height: 96px;
    background: var(--aqua);
    display: flex;
    align-items: center;
    justify-content: center;
    font-family: "Cormorant Garamond", serif;
    font-size: 30px;
    color: var(--white);
  }
</style>
</head>
<body>
  <main class="label">
    <p class="tagline">Formulated by a Naturopath</p>
    <div class="brand">
      <span class="brand-dot" aria-hidden="true"></span>
      <span class="brand-name">lumavale</span>
    </div>
    <div class="accent-strip" aria-hidden="true"></div>

    <p class="subtitle">Anti-aging therapy</p>

    <h1 class="product-name">
      <span class="primary">ORGANIC</span>
      <span class="secondary">FACIAL OIL</span>
    </h1>

    <p class="ingredients">with CoEnzyme Q10 and Rosehip Seed Oil</p>

    <div class="volume-band">100ml&nbsp;℮3.38fl.oz</div>
  </main>
</body>
</html>
```